Saltmarsh Valley Lending Flyer

I would like our main long logo with the bird and words Saltmarsh Valley Lending with pictures of what we finance along the bottom.
Car , 4x4 , boat, excavator , Cash Loans and houses
Needs to look good on leaflet and large signage.
Simple but cool looking so it stands out.

```html
<!DOCTYPE html>
<html lang="en">
<head>
<meta charset="UTF-8">
<title>Saltmarsh Valley Lending Flyer</title>
<link href="https://fonts.googleapis.com/css2?family=Cinzel:wght@600;700&family=Lato:wght@400;700;900&display=swap" rel="stylesheet">
<style>
  :root {
    --orange: #d9812f;
    --orange-deep: #c46d1d;
    --ink: #1c1c1c;
    --black: #0d0d0d;
    --white: #ffffff;
    --page: #d6d6d6;
    --text: #2a2a2a;
  }
  * { box-sizing: border-box; margin: 0; padding: 0; }
  html, body { width: 1200px; height: 1200px; overflow: hidden; background: var(--page); }
  .flyer {
    position: absolute; left: 197px; top: 30px;
    width: 806px; height: 1140px; background: var(--white);
    overflow: hidden; font-family: "Lato", sans-serif; color: var(--text);
    box-shadow: 0 10px 30px rgba(0,0,0,.25);
  }
  .hero-photo {
    position: absolute; left: 0; top: 0; width: 806px; height: 500px;
    background: linear-gradient(180deg, #5d97dc 0%, #b9d3ee 28%, #e2d6b4 45%, #cbb98f 62%, #6f8f4a 80%, #c9c2a8 100%);
  }
  .brand {
    position: absolute; top: 30px; right: 40px;
    display: flex; align-items: center; gap: 12px;
  }
  .brand-dot { width: 30px; height: 30px; border-radius: 50%; background: var(--orange); }
  .brand-name {
    font-family: "Cinzel", serif; font-weight: 700; font-size: 21px;
    line-height: 1.05; color: var(--ink);
  }
  .headline-band {
    position: absolute; left: 0; top: 480px; width: 620px; height: 185px;
    background: var(--orange);
  }
  .headline {
    position: absolute; left: 40px; top: 508px; width: 540px;
    font-family: "Cinzel", serif; font-weight: 700; font-size: 40px;
    line-height: 1.05; color: var(--ink); white-space: nowrap;
  }
  .photo-circle {
    position: absolute; border-radius: 50%;
    border: 8px solid var(--white); outline: 4px solid var(--black);
  }
  .photo-car {
    left: 570px; top: 660px; width: 480px; height: 480px;
    background: radial-gradient(circle at 40% 45%, #f4f4f4 0%, #cfd2d6 45%, #6b6f74 80%, #2c2e31 100%);
  }
  .photo-boat {
    left: 540px; top: 610px; width: 250px; height: 250px;
    background: linear-gradient(180deg, #a9c6df 0%, #e8eef2 40%, #3f6f92 62%, #24506f 100%);
  }
  .photo-advisers {
    left: 575px; top: 300px; width: 300px; height: 300px;
    background: linear-gradient(135deg, #f1ede7 0%, #d8cdbf 40%, #40495e 75%, #232b3d 100%);
  }
  .services-tab {
    position: absolute; left: 0; top: 680px; width: 250px; height: 50px;
    background: var(--black); border-radius: 0 25px 25px 0;
    color: var(--white); font-weight: 900; font-size: 31px; letter-spacing: .5px;
    padding-left: 40px; line-height: 50px;
  }
  .services-copy {
    position: absolute; left: 40px; top: 742px; width: 420px;
    font-size: 15px; line-height: 1.3; font-weight: 700;
  }
  .services-copy p + p { margin-top: 8px; }
  .loan-list { position: absolute; top: 895px; list-style: none; }
  .loan-list.col-a { left: 40px; }
  .loan-list.col-b { left: 280px; }
  .loan-item {
    display: flex; align-items: center; gap: 14px;
    height: 44px; margin-bottom: 14px;
    font-size: 19px; font-weight: 700; color: var(--ink);
  }
  .loan-icon {
    width: 44px; height: 44px; border-radius: 50%; background: var(--orange);
    display: flex; align-items: center; justify-content: center; flex: none;
  }
  .loan-icon svg { width: 26px; height: 26px; }
  .footer-curve { position: absolute; left: 0; top: 0; width: 806px; height: 1140px; pointer-events: none; }
  .footer {
    position: absolute; left: 0; bottom: 0; width: 806px; height: 70px;
    background: var(--black); color: var(--white);
    display: flex; align-items: center; justify-content: space-around;
    font-size: 17px;
  }
  .footer-item { display: flex; align-items: center; gap: 8px; }
  .footer-item svg { width: 18px; height: 18px; }
</style>
</head>
<body>
<main class="flyer">
  <div class="hero-photo" role="img" aria-label="Modern two-storey home with landscaped garden under a blue sky"></div>

  <div class="brand">
    <span class="brand-dot"></span>
    <span class="brand-name">Saltmarsh Valley<br>Lending</span>
  </div>

  <div class="headline-band"></div>
  <h1 class="headline">EXPERTS IN<br>MORTGAGE BROKING<br>AND LENDING</h1>

  <div class="photo-circle photo-car" role="img" aria-label="Front of a white car"></div>
  <div class="photo-circle photo-boat" role="img" aria-label="White motor boat cruising on the water"></div>
  <div class="photo-circle photo-advisers" role="img" aria-label="Two advisers in suits reviewing a tablet"></div>

  <svg class="footer-curve" viewBox="0 0 806 1140" aria-hidden="true">
    <path d="M560 1070 Q 690 1060 806 1030" fill="none" stroke="var(--orange)" stroke-width="4"/>
  </svg>

  <div class="services-tab">SERVICES</div>
  <div class="services-copy">
    <p>There are a number of products on the market and it is important that you find a solution that best suits your needs and serviceability.</p>
    <p>We pride ourselves on our ability to get your loans settled! We have extensive experience in all things lending, including:</p>
  </div>

  <ul class="loan-list col-a">
    <li class="loan-item">
      <span class="loan-icon"><svg viewBox="0 0 24 24" fill="#fff"><path d="M4 14l2-5h12l2 5v4h-2v-2H6v2H4z"/><circle cx="7.5" cy="14" r="1.2" fill="#d9812f"/><circle cx="16.5" cy="14" r="1.2" fill="#d9812f"/></svg></span>
      Car Loans
    </li>
    <li class="loan-item">
      <span class="loan-icon"><svg viewBox="0 0 24 24" fill="#fff"><path d="M3 14h18l-3 5H6z"/><path d="M8 14V9h6l3 5z"/></svg></span>
      Boat Loans
    </li>
    <li class="loan-item">
      <span class="loan-icon"><svg viewBox="0 0 24 24" fill="none" stroke="#fff" stroke-width="2"><rect x="3" y="7" width="18" height="10" rx="1"/><circle cx="12" cy="12" r="2.5"/></svg></span>
      Cash Loans
    </li>
  </ul>
  <ul class="loan-list col-b">
    <li class="loan-item">
      <span class="loan-icon"><svg viewBox="0 0 24 24" fill="#fff"><path d="M3 15V10l3-4h10l3 4h2v5h-2v2h-3v-2H8v2H5v-2z"/></svg></span>
      4x4 Loans
    </li>
    <li class="loan-item">
      <span class="loan-icon"><svg viewBox="0 0 24 24" fill="#fff"><rect x="3" y="14" width="12" height="4" rx="2"/><rect x="5" y="9" width="6" height="5"/><path d="M11 10l6-4 3 6h-2l-2-3-4 3z"/></svg></span>
      Excavator Loans
    </li>
    <li class="loan-item">
      <span class="loan-icon"><svg viewBox="0 0 24 24" fill="#fff"><path d="M12 4l9 8h-3v7h-4v-5h-4v5H6v-7H3z"/></svg></span>
      Houses Loans
    </li>
  </ul>

  <footer class="footer">
    <span class="footer-item">
      <svg viewBox="0 0 24 24" fill="var(--orange)"><path d="M6 3l3 0 2 5-2 1a11 11 0 006 6l1-2 5 2v3a2 2 0 01-2 2A17 17 0 014 5a2 2 0 012-2z"/></svg>
      08 8900 2741
    </span>
    <span class="footer-item">
      <svg viewBox="0 0 24 24" fill="none" stroke="var(--orange)" stroke-width="2"><rect x="3" y="6" width="18" height="12"/><path d="M3 6l9 7 9-7"/></svg>
      info@svlending.com.au
    </span>
    <span class="footer-item">
      <svg viewBox="0 0 24 24" fill="none" stroke="var(--orange)" stroke-width="2"><circle cx="12" cy="12" r="9"/><path d="M3 12h18M12 3c3 3 3 15 0 18M12 3c-3 3-3 15 0 18"/></svg>
      www.svlending.com.au
    </span>
  </footer>
</main>
</body>
</html>
```